KWT Contracting services . Building and maintenance services, optic fibre installation

Business cards and logo design.I need a logo that I can use on business cards ,workwear and on my vehicles. I would like the KWT to be the main or larger text and contracting services to be the smaller or less important text.I like monograms, modern designs and repeating patterns symbols. I am also a Gemini and my favourite number is 22 so if this can be any inspiration to help with the design. Am thinking of the using German flag colours as a his is my family’s heritage. And the other 2 main colours I wear is black and white.But any ideas are appreciated.I do not need a design that is trade specific but a design that could be used for any business.

Target Market(s)

General public

Contact Information for Business Card

KWT Contracting Services ( front of business card)

(Back of business card)
Milo Brackwood
0471539264
Maintenance services
Optic fibre and data installation

Logo Text

Logo can just be pattern or monogram or incorporate KWT . I like the gemini star sign and the number 22

Colors
ec1f27
000000
fbee3e
ffffff

Requirements
Must have
• Logo and KWT Contracting Services on the front of business card
Nice to have
• Possible use of German flag colours.
• Modern design.
• Design to be able to be used on black or white background as I want to put it on clothing

```html
<!DOCTYPE html>
<html lang="en">
<head>
<meta charset="utf-8">
<title>KWT Contracting Services – Business Card</title>
<link href="https://fonts.googleapis.com/css2?family=Open+Sans:wght@400;600;700;800&display=swap" rel="stylesheet">
<style>
  :root{
    --red:#ec1f27;
    --black:#000000;
    --yellow:#fbee3e;
    --white:#ffffff;
    --backdrop:#1b1c1f;
    --skyline:#3a0709;
  }
  *{box-sizing:border-box;margin:0;padding:0}
  html,body{width:1200px;height:927px;overflow:hidden}
  body{background:var(--backdrop);font-family:"Open Sans",Arial,sans-serif;position:relative}
  .card{position:absolute;width:520px;height:298px;top:315px;background:var(--black);overflow:hidden;
        box-shadow:0 10px 30px rgba(0,0,0,.5)}
  .card--front{left:50px}
  .card--back{left:630px}

  /* front */
  .skyline{position:absolute;left:0;right:0;bottom:0;height:62%;
           background:linear-gradient(180deg,rgba(58,7,9,0) 0%,var(--skyline) 35%,var(--skyline) 100%)}
  .brand{position:absolute;left:0;right:0;top:62px;text-align:center}
  .brand__name{display:inline-flex;align-items:center;gap:10px;font-weight:800;font-size:58px;
               line-height:1;color:var(--red);letter-spacing:2px}
  .brand__square{width:16px;height:16px;background:var(--yellow)}
  .brand__sub{font-weight:700;font-size:30px;color:var(--red);letter-spacing:1px;margin-top:6px;line-height:1}
  .brand__rule{display:flex;align-items:center;justify-content:center;gap:10px;margin-top:6px}
  .brand__rule span.line{width:90px;height:1.5px;background:var(--yellow)}
  .brand__services{color:var(--yellow);font-weight:600;font-size:16px;letter-spacing:6px}

  /* back */
  .tab{position:absolute;top:0;left:172px;width:160px;height:46px;background:var(--red);
       border-radius:0 0 14px 14px}
  .band{position:absolute;left:0;right:0;bottom:0;height:112px;background:var(--red)}
  .notch{position:absolute;left:190px;width:190px;top:186px;height:32px;background:var(--black);
         border-radius:0 0 16px 16px}
  .person{position:absolute;left:196px;top:56px;color:var(--yellow);font-size:14px;line-height:1.35}
  .person__phone{display:flex;align-items:center;gap:5px}
  .logo-mark{position:absolute;left:34px;top:118px;display:flex;align-items:center;gap:7px;
             color:var(--red);font-weight:800;font-size:38px;line-height:1}
  .logo-mark .sq{width:11px;height:11px;background:var(--yellow)}
  .divider{position:absolute;left:172px;top:110px;width:1.5px;height:56px;background:var(--red)}
  .services{position:absolute;left:186px;top:116px;color:var(--yellow);font-size:14px;line-height:1.4}
  .contact{position:absolute;left:0;right:0;bottom:24px;color:var(--yellow);font-size:13.5px;
           line-height:1.7;text-align:center}
  .contact__row{display:flex;align-items:center;justify-content:center;gap:6px}
  .contact svg{flex:none}
</style>
</head>
<body>
  <section class="card card--front" aria-label="Business card front">
    <div class="skyline" role="img" aria-label="Dark red city skyline silhouette"></div>
    <div class="brand">
      <div class="brand__name"><span class="brand__square"></span>KWT</div>
      <div class="brand__sub">CONTRACTING</div>
      <div class="brand__rule"><span class="line"></span><span class="brand__services">Services</span><span class="line"></span></div>
    </div>
  </section>

  <section class="card card--back" aria-label="Business card back">
    <div class="tab"></div>
    <div class="band"></div>
    <div class="notch"></div>

    <div class="person">
      <div class="person__name">MILO BRACKWOOD</div>
      <div class="person__phone">
        <svg width="11" height="11" viewBox="0 0 24 24" aria-hidden="true"><path fill="#fbee3e" d="M6.6 10.8a15.2 15.2 0 0 0 6.6 6.6l2.2-2.2c.3-.3.7-.4 1-.2 1.1.4 2.3.6 3.6.6.6 0 1 .4 1 1V20c0 .6-.4 1-1 1A17 17 0 0 1 3 4c0-.6.4-1 1-1h3.5c.6 0 1 .4 1 1 0 1.3.2 2.5.6 3.6.1.3 0 .7-.2 1z"/></svg>
        0471539264
      </div>
    </div>

    <div class="logo-mark"><span class="sq"></span>KWT</div>
    <div class="divider"></div>
    <div class="services">
      <div>MAINTENANCE SERVICES</div>
      <div>Optic Fibre and Data Installation</div>
    </div>

    <div class="contact">
      <div class="contact__row">
        <svg width="11" height="13" viewBox="0 0 24 28" aria-hidden="true"><path fill="#000" d="M12 0a10 10 0 0 0-10 10c0 7.5 10 18 10 18s10-10.5 10-18A10 10 0 0 0 12 0zm0 14a4 4 0 1 1 0-8 4 4 0 0 1 0 8z"/></svg>
        Unit 4/9, Harlow Crescent, Ridgefield, WA 6148
      </div>
      <div class="contact__row">
        <svg width="13" height="10" viewBox="0 0 26 20" aria-hidden="true"><path fill="#000" d="M0 0h26v20H0z"/><path d="M1 1l12 9 12-9" stroke="#ec1f27" stroke-width="2" fill="none"/></svg>
        info@kwtcontracting.com
        <svg width="11" height="11" viewBox="0 0 24 24" aria-hidden="true" style="margin-left:8px"><circle cx="12" cy="12" r="11" fill="#000"/></svg>
        www.kwtcontracting.com
      </div>
    </div>
  </section>
</body>
</html>
```